Vitamin gum packaging artwork

Artwork and branding for Brellox Ltd.'s Chewloria. Artwork should be transferable for use on blister packaging, plastic tub, or box packaging format, see pictures. Innovative packaging design ideas are also welcome. Think Glintsplash, trendy consumer good targeting 24-48 yr olds. Supermarket, convenience store, impulse purchase product NOT strictly pharmaceutical retail. Design concept should also lend itself to necessary colour/graphic changes for flavours of 'Fresh Spearmint' and 'Cool Peppermint'. Key text to include: Product name: Chewloria, Flavour, Multivitamin chewing gum, Formulated by Medical Doctors, chew two, one serving (2 pieces) provides 100% of an adults daily requirement of vitamins and minerals, nutritional supplement.

Industry/Entity Type

Plastic

```html
<!DOCTYPE html>
<html lang="en">
<head>
<meta charset="utf-8">
<title>Chewloria Peppermint – Pack Artwork</title>
<link rel="stylesheet" href="https://fonts.googleapis.com/css2?family=Baloo+2:wght@700;800&family=Lilita+One&family=Open+Sans:wght@700;800&display=swap">
<style>
  :root {
    --navy: #14206b;
    --outline-blue: #0f5fc4;
    --mint-light: #7fcf5a;
    --mint-dark: #2f8a2a;
    --white: #ffffff;
  }
  * { margin: 0; padding: 0; box-sizing: border-box; }
  html, body { width: 1200px; height: 675px; overflow: hidden; background: #1b1d20; }
  .pack {
    position: relative;
    width: 1200px;
    height: 675px;
    overflow: hidden;
    font-family: "Baloo 2", sans-serif;
    color: var(--white);
  }
  .pack-background { position: absolute; inset: 0; }

  .claim-doctors {
    position: absolute; left: 28px; top: 24px;
    font-weight: 800; font-size: 21px; line-height: 25px; letter-spacing: 0.3px;
    text-transform: uppercase;
  }

  .requirement { font-weight: 800; text-transform: uppercase; }
  .requirement-title, .requirement-item {
    text-shadow: -1.5px -1.5px 0 var(--navy), 1.5px -1.5px 0 var(--navy),
                 -1.5px 1.5px 0 var(--navy), 1.5px 1.5px 0 var(--navy);
  }
  .requirement-title {
    position: absolute; right: 32px; top: 22px;
    font-size: 23px; line-height: 30px; white-space: nowrap;
  }
  .requirement-list { list-style: none; }
  .requirement-item {
    position: absolute; z-index: 3; display: flex; align-items: center; gap: 8px;
    font-size: 22px; line-height: 28px; white-space: nowrap;
  }
  .requirement-item--vitamins { left: 943px; top: 63px; }
  .requirement-item--minerals { left: 963px; top: 99px; }
  .requirement-item--nutritional { left: 983px; top: 137px; }
  .bolt { width: 12px; height: 22px; flex: none; }

  .mint-leaves {
    position: absolute; z-index: 1; left: 690px; top: 92px; width: 240px; height: 170px;
    border-radius: 50% 45% 55% 40%;
    background: radial-gradient(ellipse at 55% 50%, var(--mint-light) 0%, var(--mint-dark) 60%, rgba(47,138,42,0) 72%);
  }

  .gum-pieces {
    position: absolute; left: 52px; top: 190px; width: 206px; height: 218px;
    border-radius: 40px;
    background: radial-gradient(ellipse at 50% 50%, #ffffff 0%, #e9eef3 55%, rgba(200,212,224,0) 75%);
  }

  .product-name {
    position: absolute; z-index: 2; left: 326px; top: 222px;
    font-family: "Lilita One", sans-serif; font-weight: 400; font-size: 92px; line-height: 100px;
    text-transform: uppercase; letter-spacing: 1px;
    transform: skewX(-8deg);
    color: var(--white);
    -webkit-text-stroke: 3px var(--outline-blue);
    paint-order: stroke fill;
    text-shadow: 3px 4px 0 var(--navy), 0 0 10px rgba(15,95,196,0.6);
  }
  .flavour-name {
    position: absolute; z-index: 2; left: 551px; top: 334px;
    font-family: "Lilita One", sans-serif; font-weight: 400; font-size: 52px; line-height: 58px;
    text-transform: uppercase; letter-spacing: 1px;
    color: var(--white);
    -webkit-text-stroke: 2px var(--navy);
    paint-order: stroke fill;
    text-shadow: 2px 3px 3px rgba(20,32,107,0.5);
  }

  .serving-badge { position: absolute; right: 0; top: 508px; width: 395px; height: 108px; }
  .serving-badge-text {
    position: absolute; right: 12px; top: 538px;
    font-family: "Open Sans", sans-serif; font-weight: 800; font-size: 37px; line-height: 46px;
    white-space: nowrap;
    text-shadow: 1px 2px 2px rgba(0,0,0,0.35);
  }

  .count-pill {
    position: absolute; left: 46px; top: 558px; width: 311px; height: 78px;
    border-radius: 40px; border: 4px solid var(--white);
    background: linear-gradient(180deg, #b8c7ee 0%, #6f86d8 45%, #2e3fb0 100%);
    box-shadow: 0 3px 8px rgba(0,0,0,0.35);
    display: flex; align-items: center; gap: 12px; padding-left: 24px;
  }
  .count-icon { width: 46px; height: 46px; flex: none; }
  .count-text {
    font-family: "Open Sans", sans-serif; font-weight: 800; font-size: 42px;
    color: var(--navy); line-height: 1;
  }

  .maker {
    position: absolute; right: 32px; top: 628px;
    font-weight: 700; font-size: 17px; letter-spacing: 1px; text-transform: uppercase;
  }
</style>
</head>
<body>
<main class="pack">
  <svg class="pack-background" width="1200" height="675" viewBox="0 0 1200 675" aria-hidden="true">
    <defs>
      <linearGradient id="base" x1="0" y1="0" x2="0" y2="1">
        <stop offset="0" stop-color="#0a8ac8"/>
        <stop offset="0.55" stop-color="#1272c8"/>
        <stop offset="1" stop-color="#0b3f98"/>
      </linearGradient>
      <radialGradient id="purpleWash" cx="1" cy="0.75" r="0.6">
        <stop offset="0" stop-color="#3d1f8c"/>
        <stop offset="0.6" stop-color="#5a3bb0" stop-opacity="0.75"/>
        <stop offset="1" stop-color="#5a3bb0" stop-opacity="0"/>
      </radialGradient>
      <radialGradient id="centreGlow" cx="0.5" cy="0.5" r="0.5">
        <stop offset="0" stop-color="#ffffff"/>
        <stop offset="0.6" stop-color="#ffffff"/>
        <stop offset="0.85" stop-color="#ffffff" stop-opacity="0.55"/>
        <stop offset="1" stop-color="#ffffff" stop-opacity="0"/>
      </radialGradient>
      <radialGradient id="cornerLight" cx="0.95" cy="0.05" r="0.35">
        <stop offset="0" stop-color="#ffffff"/>
        <stop offset="0.5" stop-color="#d6f3ff" stop-opacity="0.7"/>
        <stop offset="1" stop-color="#d6f3ff" stop-opacity="0"/>
      </radialGradient>
    </defs>
    <rect width="1200" height="675" fill="url(#base)"/>
    <rect width="1200" height="675" fill="url(#purpleWash)"/>
    <rect width="1200" height="675" fill="url(#cornerLight)"/>
    <ellipse cx="610" cy="300" rx="360" ry="200" fill="url(#centreGlow)"/>
    <path d="M0 480 C 260 600, 620 640, 1200 560 L1200 675 L0 675 Z" fill="#0d4fb0" opacity="0.45"/>
    <path d="M0 495 C 280 610, 640 640, 1200 575" fill="none" stroke="#4aa8f0" stroke-width="3" opacity="0.6"/>
    <path d="M0 520 C 300 640, 700 660, 1200 600" fill="none" stroke="#3b8fe0" stroke-width="2" opacity="0.45"/>
  </svg>

  <p class="claim-doctors">Formulated by<br>Medical Doctors</p>

  <section class="requirement">
    <h2 class="requirement-title">Adults Daily Requirement</h2>
    <ul class="requirement-list">
      <li class="requirement-item requirement-item--vitamins"><svg class="bolt" viewBox="0 0 12 22"><path d="M8 0 L1 12 H6 L3 22 L11 8 H6 Z" fill="#ffffff"/></svg>Vitamins</li>
      <li class="requirement-item requirement-item--minerals"><svg class="bolt" viewBox="0 0 12 22"><path d="M8 0 L1 12 H6 L3 22 L11 8 H6 Z" fill="#ffffff"/></svg>Minerals</li>
      <li class="requirement-item requirement-item--nutritional"><svg class="bolt" viewBox="0 0 12 22"><path d="M8 0 L1 12 H6 L3 22 L11 8 H6 Z" fill="#ffffff"/></svg>Nutritional</li>
    </ul>
  </section>

  <div class="gum-pieces" role="img" aria-label="Two white pellets of chewing gum"></div>
  <div class="mint-leaves" role="img" aria-label="Sprig of fresh mint leaves"></div>

  <h1 class="product-name">Chewloria</h1>
  <p class="flavour-name">Pepermint</p>

  <svg class="serving-badge" viewBox="0 0 395 108" aria-hidden="true">
    <defs>
      <linearGradient id="bannerFill" x1="0" y1="0" x2="0" y2="1">
        <stop offset="0" stop-color="#8fd12a"/>
        <stop offset="1" stop-color="#3a9a1c"/>
      </linearGradient>
    </defs>
    <path d="M36 0 L395 6 L395 100 L0 108 Z" fill="url(#bannerFill)"/>
  </svg>
  <p class="serving-badge-text">100% of an adults</p>

  <div class="count-pill">
    <svg class="count-icon" viewBox="0 0 46 46" aria-hidden="true">
      <rect x="6" y="4" width="20" height="30" rx="6" transform="rotate(35 16 19)" fill="#ffffff"/>
      <rect x="18" y="14" width="20" height="30" rx="6" transform="rotate(35 28 29)" fill="#f1f4f8" stroke="#c9d3e6" stroke-width="1"/>
    </svg>
    <span class="count-text">2 Gums</span>
  </div>

  <p class="maker">Brellox Ltd.'s</p>
</main>
</body>
</html>
```